Human-Centred Systems Design

We need to design the look and feel for an innovation company with software products for solving complex IT problems following socio-technical theory thinking. The company is heavy in designing of complex systems (like an architect shop). The new design will form the foundation of our brand moving forward. We will approach software projects as if one is building a skyscraper or a bridge. We want to humanize technology and not the other way around. Our target groups will be healthcare and the environment. We will be able to take complex problems and turn them into amazing IT solutions that improve the quality of life for people.

Here are more fragments of ideas that can help:
===============

Motivation

The technology described in the application, coincides with “Steer-Through-Mesh” concept of Marvin Oldroyd, which suggests managing a business by managing an informational representation of it : Marvin had the following vision:

"Imagine an enterprise design model that defines the behavior of an entire business. Imagine making this model a part of the corporate informational infrastructure, implementing it on technology that connects all relevant sources and users of information and affords maximum sharing among all parts of the firm. Managers could respond to the read-outs appearing on the console, modifying the flight plan en route based on changes in external conditions, monitoring the performance of delegated responsibilities, sending coordinated directions to subsidiary functions, and experiencing exhilaration upon their execution. It constitutes institutional memory and intelligence, which augment management's ability to run the business”.

This product does what Mr. Oldroyd envisioned.

The Objective

QLT offers software products for the specification, construction, assembly, and ongoing management of a digital representation that is an exact mirror image of an enterprise. The main idea is the capability of managing the enterprise by managing an information technology representation of it through software. The idea is to manage the enterprise as a total system involving all aspects of operations. That makes the enterprise and all its information technology representation is inseparable. The implication is that the management of change at the business and IT infrastructure levels are unified. For example, by reconfiguring the information representation of the enterprise one can change business performance. By changing the configuration of the business representation one can actually change the organization’s ability to respond to internal and external events. Management leadership can act with the aid of technology to better respond and improve their ability to guide the organization. The knowledge management feature of the digital representation of the enterprise enables managers to monitor the impact of change and therefore help management assess risk and determine whether mitigating responses are necessary.

The technology and product defines a new approach for the design, implementation, and ongoing execution of software systems that are truly business-like rather than applications and workflows.

```html
<!DOCTYPE html>
<html lang="en">
<head>
<meta charset="utf-8">
<title>Keystone Software – Human-Centred Systems Design</title>
<link href="https://fonts.googleapis.com/css2?family=Lato:wght@300;400&family=Ubuntu:wght@400;500&display=swap" rel="stylesheet">
<style>
:root{
  --header-top:#3b3b3b;
  --header-bottom:#000000;
  --accent:#2aa6d8;
  --teal-band:#4193a8;
  --icon-disc:#cde8ee;
  --icon-ink:#2d4a55;
  --ink:#333333;
  --heading:#3d3f45;
  --link:#2f8aa3;
  --panel:#ececec;
  --tab-off:#a9a9a9;
  --footer:#222222;
  --footer-link:#2d9fc9;
  --white:#ffffff;
}
*{box-sizing:border-box;margin:0;padding:0}
html,body{width:1023px;height:1200px;overflow:hidden}
body{position:relative;background:var(--white);font-family:Arial,Helvetica,sans-serif;color:var(--ink)}
.abs{position:absolute}

/* header */
.site-header{position:absolute;left:0;top:0;width:1023px;height:113px;background:linear-gradient(var(--header-top),#1a1a1a 55%,var(--header-bottom))}
.brand-name{left:119px;top:14px;font-family:'Lato',sans-serif;font-weight:400;font-size:26px;color:var(--white);line-height:1}
.brand-tag{left:120px;top:45px;font-family:'Lato',sans-serif;font-weight:400;font-size:12px;color:var(--accent);letter-spacing:.3px}
.util-links{left:751px;top:43px;font-size:9.5px;color:var(--accent);white-space:nowrap}
.util-links span{color:#9ab}
.main-nav{left:113px;top:68px;width:799px;height:39px;border-radius:20px;background:linear-gradient(#2b2d31,#1a1b1e);display:flex;align-items:center;padding:0 6px;gap:4px}
.nav-item{flex:1;height:27px;border-radius:14px;background:linear-gradient(#3d4045,#222428);box-shadow:inset 0 1px 0 rgba(255,255,255,.12);color:var(--white);font-family:'Ubuntu',sans-serif;font-size:11.5px;display:flex;align-items:center;justify-content:center}
.nav-item.is-active{background:linear-gradient(#ffffff,#cfd3d8 60%,#aeb3b9);color:#333}

/* hero */
.hero{left:0;top:113px;width:1023px;height:341px;background:linear-gradient(100deg,#6f97ab 0%,#2f5d72 30%,#12313f 55%,#24505e 75%,#101c24 100%)}
.hero-title{left:348px;top:202px;font-family:'Lato',sans-serif;font-weight:300;font-size:27px;color:var(--white);line-height:1}
.hero-copy{left:350px;top:234px;width:275px;font-size:12px;line-height:14.3px;color:#cfe3ea}
.hero-arrow{width:52px;height:52px}

/* features */
.features{left:0;top:454px;width:1023px;height:226px;background:var(--teal-band)}
.feature{position:absolute;top:0;width:240px;text-align:center}
.feature-icon{width:56px;height:56px;border-radius:50%;background:var(--icon-disc);margin:25px auto 0;display:flex;align-items:center;justify-content:center}
.feature-title{font-family:'Lato',sans-serif;font-weight:300;font-size:27px;color:var(--white);margin-top:17px;line-height:1}
.feature-copy{font-size:12px;line-height:14.5px;color:#e6f2f5;margin-top:12px}

/* how it works */
.section-title{font-family:'Lato',sans-serif;font-weight:300;font-size:27px;color:var(--heading);line-height:1}
.tabs{left:113px;top:766px;display:flex}
.tab{width:81px;height:28px;background:var(--tab-off);color:var(--white);font-size:10.5px;display:flex;align-items:center;justify-content:center;border-right:1px solid #ddd}
.tab.is-active{background:var(--panel);color:#333}
.steps-panel{left:113px;top:794px;width:499px;height:191px;background:var(--panel)}
.step-photo{left:123px;top:804px;width:202px;height:169px;background:var(--white);padding:4px}
.step-photo div{width:100%;height:100%;background:linear-gradient(135deg,#e9edf0,#b8c2c8 55%,#6d747a)}
.step-copy{left:340px;top:830px;width:260px;font-size:12px;line-height:14.3px;color:#333}
.step-copy p+p{margin-top:14px}

/* services */
.service-list{left:673px;top:767px;list-style:none}
.service-list li{height:25.6px;font-size:12px;color:var(--link);display:flex;align-items:center;white-space:nowrap}
.service-list svg{margin-right:7px}

/* footer */
.site-footer{left:0;top:1035px;width:1023px;height:165px;background:var(--footer)}
.footer-brand{left:117px;top:1062px;font-family:'Lato',sans-serif;font-weight:400;font-size:17px;color:var(--white);line-height:1}
.copyright{left:119px;top:1090px;font-size:9.5px;color:#ddd}
.footer-col h3{font-family:'Ubuntu',sans-serif;font-weight:400;font-size:14.5px;color:var(--white);margin-bottom:9px}
.footer-col ul{list-style:none}
.footer-col li{font-size:10px;color:var(--footer-link);height:19px;display:flex;align-items:center;letter-spacing:.3px}
.footer-col li::before{content:"";border-left:3px solid #ccc;border-top:2.5px solid transparent;border-bottom:2.5px solid transparent;margin-right:7px}
.email-field{left:732px;top:1088px;width:158px;height:21px;background:#2b2b2b;border:1px solid #444;border-radius:3px;font-size:10px;color:#aaa;padding:4px 12px}
.subscribe{left:825px;top:1119px;width:68px;height:22px;border-radius:4px;background:#2a9fc6;color:var(--white);font-family:'Ubuntu',sans-serif;font-size:10px;display:flex;align-items:center;justify-content:center}
</style>
</head>
<body>

<header class="site-header">
  <div class="abs brand-name">Keystone Software</div>
  <div class="abs brand-tag">HUMAN-CENTRED SYSTEMS DESIGN</div>
  <div class="abs util-links">Support &nbsp;<span>|</span>&nbsp; FAQs &nbsp;<span>|</span>&nbsp; Site Map &nbsp;<span>|</span>&nbsp; Help</div>
  <nav class="abs main-nav">
    <div class="nav-item is-active">Home</div>
    <div class="nav-item">About us</div>
    <div class="nav-item">Products</div>
    <div class="nav-item">Download</div>
    <div class="nav-item">Services</div>
    <div class="nav-item">Contact us</div>
  </nav>
</header>

<section class="abs hero" role="img" aria-label="Glass skyscraper beside a businessman holding a tablet, overlaid with digital data">
</section>
<div class="abs hero-title">LOREM IPSUM DOLOR</div>
<p class="abs hero-copy">Duis aute irure dolor in reprehenderit in voluptate velit esse cillum dolore eu fugiat nulla pariatur. Excepteur sint occaecat cupidatat non proident, sunt in culpa qui officia deserunt mollit anim id est laborum.</p>
<svg class="abs hero-arrow" style="left:96px;top:271px" viewBox="0 0 52 52" aria-label="Previous slide"><circle cx="26" cy="26" r="22" fill="none" stroke="#fff" stroke-width="4"/><path d="M30 15 L19 26 L30 37" fill="none" stroke="#fff" stroke-width="5"/></svg>
<svg class="abs hero-arrow" style="left:876px;top:271px" viewBox="0 0 52 52" aria-label="Next slide"><circle cx="26" cy="26" r="22" fill="none" stroke="#fff" stroke-width="4"/><path d="M22 15 L33 26 L22 37" fill="none" stroke="#fff" stroke-width="5"/></svg>

<section class="abs features">
  <div class="feature" style="left:106px">
    <div class="feature-icon"><svg width="30" height="30" viewBox="0 0 30 30"><circle cx="15" cy="15" r="9" fill="none" stroke="var(--icon-ink)" stroke-width="5" stroke-dasharray="4 3"/><circle cx="15" cy="15" r="5" fill="var(--icon-ink)"/><path d="M9 22 L20 11" stroke="var(--icon-disc)" stroke-width="3"/></svg></div>
    <h2 class="feature-title">ADVANTAGES</h2>
    <p class="feature-copy">Lorem ipsum dolor sit amet, consectetur adipisicing elit, sed do eiusmod tempor incididunt ut labore et dolore magna aliqua.</p>
  </div>
  <div class="feature" style="left:383px">
    <div class="feature-icon"><svg width="32" height="32" viewBox="0 0 32 32"><circle cx="16" cy="17" r="12" fill="none" stroke="var(--icon-ink)" stroke-width="3"/><circle cx="16" cy="17" r="6" fill="none" stroke="var(--icon-ink)" stroke-width="3"/><path d="M16 17 L27 6" stroke="var(--icon-ink)" stroke-width="2.5"/></svg></div>
    <h2 class="feature-title">MISSION</h2>
    <p class="feature-copy">Sed ut perspiciatis, unde omnis iste natus error sit voluptatem accusantium doloremque laudantium, totam rem aperiam.</p>
  </div>
  <div class="feature" style="left:660px">
    <div class="feature-icon"><svg width="32" height="32" viewBox="0 0 32 32"><path d="M11 16 a5 5 0 1 1 10 0 c0 3 -2 4 -2 6 h-6 c0 -2 -2 -3 -2 -6z" fill="none" stroke="var(--icon-ink)" stroke-width="2"/><path d="M13 25 h6 M14 27.5 h4" stroke="var(--icon-ink)" stroke-width="2"/><path d="M16 4 v3 M6 10 l2 2 M26 10 l-2 2 M3 17 h3 M26 17 h3" stroke="var(--icon-ink)" stroke-width="2"/></svg></div>
    <h2 class="feature-title">VISION</h2>
    <p class="feature-copy">Lorem ipsum dolor sit amet, consectetur adipisicing elit, sed do eiusmod tempor incididunt ut labore et dolore magna aliqua.</p>
  </div>
</section>

<h2 class="abs section-title" style="left:115px;top:727px">HOW IT WORKS</h2>
<div class="abs tabs">
  <div class="tab is-active">STEP 1</div>
  <div class="tab">STEP 2</div>
  <div class="tab">STEP 3</div>
</div>
<div class="abs steps-panel"></div>
<div class="abs step-photo"><div role="img" aria-label="Business team working at laptops in a bright office"></div></div>
<div class="abs step-copy">
  <p>At vero eos et accusamus et iusto odio dignissimos ducimus, qui blanditiis praesentium voluptatum deleniti atque corrupti, quos dolores et quas molestias excepturi sint,</p>
  <p>Obcaecati cupiditate non provident, similique sunt in culpa, qui officia deserunt mollitia animi, id est laborum et dolorum fuga.</p>
</div>

<h2 class="abs section-title" style="left:669px;top:727px">SERVICES</h2>
<ul class="abs service-list">
  <li><svg width="7" height="9" viewBox="0 0 7 9"><path d="M1 1 L5 4.5 L1 8" fill="none" stroke="#777" stroke-width="2"/></svg>At vero eos et accusamus et iusto odio</li>
  <li><svg width="7" height="9" viewBox="0 0 7 9"><path d="M1 1 L5 4.5 L1 8" fill="none" stroke="#777" stroke-width="2"/></svg>Qui blanditiis praesentium voluptatum</li>
  <li><svg width="7" height="9" viewBox="0 0 7 9"><path d="M1 1 L5 4.5 L1 8" fill="none" stroke="#777" stroke-width="2"/></svg>Nam libero tempore, cum soluta nobis est</li>
  <li><svg width="7" height="9" viewBox="0 0 7 9"><path d="M1 1 L5 4.5 L1 8" fill="none" stroke="#777" stroke-width="2"/></svg>Temporibus autem quibusdam et aut</li>
  <li><svg width="7" height="9" viewBox="0 0 7 9"><path d="M1 1 L5 4.5 L1 8" fill="none" stroke="#777" stroke-width="2"/></svg>At vero eos et accusamus et iusto odio</li>
  <li><svg width="7" height="9" viewBox="0 0 7 9"><path d="M1 1 L5 4.5 L1 8" fill="none" stroke="#777" stroke-width="2"/></svg>Qui blanditiis praesentium voluptatum</li>
  <li><svg width="7" height="9" viewBox="0 0 7 9"><path d="M1 1 L5 4.5 L1 8" fill="none" stroke="#777" stroke-width="2"/></svg>Nam libero tempore, cum soluta nobis est</li>
  <li><svg width="7" height="9" viewBox="0 0 7 9"><path d="M1 1 L5 4.5 L1 8" fill="none" stroke="#777" stroke-width="2"/></svg>Temporibus autem quibusdam et aut</li>
  <li><svg width="7" height="9" viewBox="0 0 7 9"><path d="M1 1 L5 4.5 L1 8" fill="none" stroke="#777" stroke-width="2"/></svg>Nam libero tempore, cum soluta nobis est</li>
</ul>

<footer class="abs site-footer"></footer>
<div class="abs footer-brand">Keystone</div>
<div class="abs copyright">© Copyright Keystone 2014</div>
<div class="abs footer-col" style="left:289px;top:1060px">
  <h3>Why Us</h3>
  <ul><li>Our Clients</li><li>Technology</li><li>Soft Labs</li></ul>
</div>
<div class="abs footer-col" style="left:391px;top:1060px">
  <h3>Quick Links</h3>
  <ul><li>Lorem ipsum dolor</li><li>Amet consectetuer</li><li>Mauris vel tortor vitae</li><li>Nibh condimentum</li></ul>
</div>
<div class="abs footer-col" style="left:562px;top:1060px">
  <h3>Support</h3>
  <ul><li>Nibh condimentum</li><li>Integer ac lacus</li><li>Sociis natoque</li><li>Enatibus et magnis</li></ul>
</div>
<div class="abs footer-col" style="left:732px;top:1060px">
  <h3>Newsletter:</h3>
</div>
<div class="abs email-field">Enter your email here</div>
<div class="abs subscribe">SUBSCRIBE</div>

</body>
</html>
```